VORALUX SYSTEMS BUSINESS CARD DESIGN

WE WANT COMPLETE NEW DESIGN OF OUR BUSINESS CARD. WE ARE AN INTEGRATION COMPANY, WHERE WE INTEGRATE IOT/SMART SYSTEMS TO HOMES AND CORPORATE CUSTOMERS. WE SUPPLY AND INSTALL AUTOMATION PRODUCTS. THE FINAL DESIGN SHOULD COMMUNICATE TECHNOLOGY. THE CARD DESIGN SHOULD BE VERY IMPACT FULL. LOGO NEEDS TO BE THERE. IT WOULD NICE IF THE DESIGN WAS CLEAN. COLORS IS UP TO DESIGNER TO PLAY WITH, OR CAN STICK TO CORPORATE COLORS (FOLLOW LOGO). I HAVE ADDED FEW REFERENCE PHOTOS TO DRAW INSPIRATION MAYBE. I HAVE ADDED A HEX DESIGN, ITS NOT NECESSARY TO USE THIS DESIGN, ITS UPTO DESIGNER, JUST ADDED IF NEEDED TO PLAY WITH DESIGN.

Target Market(s)

Private end users and corporate clients

Industry/Entity Type

technology, home automation, home theaters, building management systems, IOT

Contact Information for Business Card

It should include Employee name, personal number, office number, email address, both in English and arabic. DETAILS TO INCLUDE :DANIEL MARUVEN, MOBILE 0097150738219,OFFCIE 009714368174, DANIEL@VORALUXSYS.CO

Requirements
Must have
• Should feel like a technology company from design. Details both and in English and arabic (or at least have provision for arabic in design).
Nice to have
• I would like logo on one side, and details on the other side. Logo design side should communicate technology with logo. Other side can be clean just with information or also have some design aspects following from logo side. it would be interesting to see submissions with square design as well (that looks like an app Icon). colors could be of logo, red black grey and white. I have added some designs to draw inspiration from

```html
<!DOCTYPE html>
<html lang="en">
<head>
<meta charset="utf-8">
<title>Voralux Systems – Business Card</title>
<link href="https://fonts.googleapis.com/css2?family=Roboto:wght@400;500;700&display=swap" rel="stylesheet">
<style>
  :root {
    --page-bg: #ffffff;
    --card-dark: #0d1d32;
    --card-mid: #12344d;
    --card-light: #064b69;
    --hex-fill: #0b1b2f;
    --silver: #e6e8ea;
    --silver-shade: #1b1f24;
    --text-light: #ffffff;
    --accent-red: #d9344c;
  }
  html, body {
    margin: 0;
    padding: 0;
    width: 1200px;
    height: 1200px;
    overflow: hidden;
    background: var(--page-bg);
  }
  .canvas {
    position: relative;
    width: 1200px;
    height: 1200px;
  }
  .card {
    position: absolute;
    left: 205px;
    width: 798px;
    height: 456px;
    box-shadow: 8px 10px 12px rgba(0, 0, 0, 0.35);
  }
  .card--front { top: 121px; }
  .card--back { top: 631px; }
  .card svg {
    display: block;
    width: 100%;
    height: 100%;
  }
  .bg-start { stop-color: var(--card-dark); }
  .bg-mid { stop-color: var(--card-mid); }
  .bg-end { stop-color: var(--card-light); }
  .groove-shade {
    fill: none;
    stroke: var(--silver-shade);
    stroke-width: 5;
    stroke-linejoin: round;
  }
  .groove-light {
    fill: none;
    stroke: var(--silver);
    stroke-width: 3;
    stroke-linejoin: round;
  }
  .hex-main { fill: var(--hex-fill); }
  .hex-side { fill: #0c1e34; }
  .brand-name {
    font-family: "Roboto", sans-serif;
    font-weight: 700;
    fill: var(--text-light);
  }
  .person-name {
    font-family: "Roboto", sans-serif;
    font-weight: 500;
    font-size: 60px;
    letter-spacing: 1.5px;
    fill: var(--text-light);
  }
  .person-title {
    font-family: "Roboto", sans-serif;
    font-weight: 400;
    font-size: 50px;
    fill: var(--accent-red);
  }
  .contact-line {
    font-family: "Roboto", sans-serif;
    font-weight: 400;
    font-size: 34px;
    fill: var(--text-light);
  }
  .icon { fill: var(--accent-red); }
  .icon-outline {
    fill: none;
    stroke: var(--accent-red);
    stroke-width: 3;
  }
</style>
</head>
<body>
<main class="canvas">

  <!-- Front: identity and contact details -->
  <section class="card card--front" aria-label="Business card front">
    <svg viewBox="0 0 1276 729" xmlns="http://www.w3.org/2000/svg">
      <defs>
        <linearGradient id="cardGradient" x1="0" y1="0" x2="1" y2="0">
          <stop offset="0" class="bg-start"/>
          <stop offset="0.55" class="bg-mid"/>
          <stop offset="1" class="bg-end"/>
        </linearGradient>
      </defs>
      <rect width="1276" height="729" fill="url(#cardGradient)"/>

      <!-- Side hexagon fragments -->
      <g class="hex-frame">
        <polygon class="hex-side" points="255,153 282,102 377,102 407,153"/>
        <polygon class="hex-side" points="257,579 284,629 380,629 407,577"/>
        <polygon class="hex-side" points="187,192 130,192 82,274 112,324"/>
        <polygon class="hex-side" points="112,407 82,452 130,537 185,537"/>
        <polygon class="hex-side" points="480,192 534,192 584,274 557,324"/>
        <polygon class="hex-side" points="557,407 584,452 537,535 482,535"/>
        <g class="groove-shade" transform="translate(2,3)">
          <polyline points="255,153 282,102 377,102 407,153"/>
          <polyline points="257,579 284,629 380,629 407,577"/>
          <polyline points="187,192 130,192 82,274 112,324"/>
          <polyline points="112,407 82,452 130,537 185,537"/>
          <polyline points="480,192 534,192 584,274 557,324"/>
          <polyline points="557,407 584,452 537,535 482,535"/>
          <line x1="115" y1="0" x2="209" y2="155"/>
          <line x1="459" y1="577" x2="550" y2="729"/>
          <line x1="0" y1="363" x2="90" y2="363"/>
          <line x1="577" y1="363" x2="1276" y2="363"/>
        </g>
        <g class="groove-light">
          <polyline points="255,153 282,102 377,102 407,153"/>
          <polyline points="257,579 284,629 380,629 407,577"/>
          <polyline points="187,192 130,192 82,274 112,324"/>
          <polyline points="112,407 82,452 130,537 185,537"/>
          <polyline points="480,192 534,192 584,274 557,324"/>
          <polyline points="557,407 584,452 537,535 482,535"/>
          <line x1="115" y1="0" x2="209" y2="155"/>
          <line x1="459" y1="577" x2="550" y2="729"/>
          <line x1="0" y1="363" x2="90" y2="363"/>
          <line x1="577" y1="363" x2="1276" y2="363"/>
        </g>
      </g>

      <!-- Central hexagon with company name -->
      <polygon class="hex-main" points="210,155 452,153 577,363 459,577 212,579 90,363"/>
      <polygon class="groove-shade" transform="translate(2,3)" points="210,155 452,153 577,363 459,577 212,579 90,363"/>
      <polygon class="groove-light" points="210,155 452,153 577,363 459,577 212,579 90,363"/>
      <text class="brand-name" x="333" y="352" font-size="40" text-anchor="middle" letter-spacing="1">VORALUX SYSTEMS</text>

      <!-- Name and title -->
      <text class="person-name" x="1184" y="134" text-anchor="end">DANIEL MARUVEN</text>
      <text class="person-title" x="1184" y="217" text-anchor="end">Title</text>

      <!-- Contacts -->
      <text class="contact-line" x="1140" y="452" text-anchor="end">0097150738219</text>
      <path class="icon" d="M1163,425 l6,-2 l5,10 l-4,3 q2,7 8,12 l4,-3 l8,7 l-3,5 q-10,2 -18,-10 q-8,-12 -6,-22 z"/>

      <text class="contact-line" x="1144" y="542" text-anchor="end">009714368174</text>
      <rect class="icon-outline" x="1163" y="517" width="14" height="24" rx="2"/>
      <line class="icon-outline" x1="1167" y1="536" x2="1173" y2="536"/>

      <text class="contact-line" x="1140" y="632" text-anchor="end">daniel@voraluxsys.co</text>
      <rect class="icon" x="1157" y="613" width="24" height="17" rx="1"/>
      <polyline points="1158,614 1169,623 1180,614" fill="none" stroke="var(--hex-fill)" stroke-width="2"/>
    </svg>
  </section>

  <!-- Back: company name side -->
  <section class="card card--back" aria-label="Business card back">
    <svg viewBox="0 0 1276 729" xmlns="http://www.w3.org/2000/svg">
      <defs>
        <linearGradient id="cardGradientBack" x1="0" y1="0" x2="1" y2="0">
          <stop offset="0" class="bg-start"/>
          <stop offset="0.55" class="bg-mid"/>
          <stop offset="1" class="bg-end"/>
        </linearGradient>
      </defs>
      <rect width="1276" height="729" fill="url(#cardGradientBack)"/>

      <g class="groove-shade" transform="translate(2,3)">
        <line x1="0" y1="362" x2="1276" y2="362"/>
        <line x1="1162" y1="0" x2="727" y2="729"/>
      </g>
      <g class="groove-light">
        <line x1="0" y1="362" x2="1276" y2="362"/>
        <line x1="1162" y1="0" x2="727" y2="729"/>
      </g>

      <text class="brand-name" x="92" y="560" font-size="68" letter-spacing="2">VORALUX SYSTEMS</text>
    </svg>
  </section>

</main>
</body>
</html>
```